Danica Pruett Interiors business cards

We need a DOUBLE SIDED business card design that is simple, elegant and modern. We are a rapidly growing Interior Design Firm, and our brand colours are blush pink, navy, and antique gold, so we require some or all of these colours to be used. The final design should portray elegance, simplicity, and have a modern feel. We have upload inspiration photos that have the feel we're looking for.

Industry/Entity Type

Interior Design

Contact Information for Business Card

Contact information and LOGO

Colors
EB3D1F
EC4F4E
F09395
F8D3D4
FCEDEE

Requirements
Must have
• Navy, the right shade of blush pink, and antique gold

```html
<!DOCTYPE html>
<html lang="en">
<head>
<meta charset="utf-8">
<title>Danica Pruett Interiors – Business Cards</title>
<link rel="stylesheet" href="https://fonts.googleapis.com/css2?family=Arimo:wght@400;700&display=swap">
<style>
  :root {
    --backdrop: #ebebeb;
    --blush-light: #f8d3d4;
    --blush: #efb3a4;
    --blush-deep: #e39a86;
    --blush-pale: #fcedee;
    --panel: #ffffff;
    --frame: #6e2f2c;
    --navy: #1b2a5e;
    --gold: #8a7229;
    --ink: #555555;
    --rule: #7a7a7a;
  }
  * { box-sizing: border-box; margin: 0; padding: 0; }
  html, body { width: 1200px; height: 802px; overflow: hidden; }
  body {
    background: var(--backdrop);
    font-family: "Arimo", Arial, sans-serif;
    position: relative;
  }
  .card {
    position: absolute;
    top: 246px;
    width: 540px;
    height: 310px;
    box-shadow: 0 10px 24px rgba(0,0,0,.18);
    overflow: hidden;
  }
  .card--front { left: 45px; }
  .card--back { left: 615px; }
  .card__pattern {
    position: absolute; inset: 0;
    background:
      linear-gradient(135deg, var(--blush-light) 0%, var(--blush) 30%, var(--blush-pale) 48%, var(--blush-deep) 70%, var(--blush-light) 100%);
  }
  .card__frame {
    position: absolute;
    top: 26px; left: 24px; right: 24px; bottom: 26px;
    border: 2px solid var(--frame);
  }
  .card__panel {
    position: absolute;
    top: 32px; left: 32px; right: 32px; bottom: 32px;
    background: var(--panel);
  }
  /* front */
  .brand-mark {
    position: absolute; top: 30px; left: 34px;
    font-size: 11px; color: var(--navy); font-weight: 700;
    letter-spacing: .5px;
  }
  .person { position: absolute; top: 96px; left: 34px; width: 160px; text-align: right; }
  .person__name { font-size: 21px; font-weight: 700; color: var(--gold); }
  .person__role { font-size: 14px; color: var(--ink); margin-top: 4px; }
  .divider { position: absolute; top: 84px; left: 212px; width: 1px; height: 72px; background: var(--rule); }
  .contacts { position: absolute; top: 80px; left: 228px; list-style: none; }
  .contacts li { display: flex; align-items: center; gap: 8px; font-size: 15px; color: var(--ink); line-height: 26px; }
  .contacts svg { width: 12px; height: 12px; fill: var(--gold); flex: none; }
  .address-line {
    position: absolute; left: 30px; right: 30px; bottom: 30px;
    display: flex; align-items: center; gap: 10px;
    font-size: 14px; color: var(--ink); white-space: nowrap;
  }
  .address-line::before, .address-line::after { content: ""; flex: 1; height: 1px; background: var(--rule); }
  /* back */
  .brand-name {
    position: absolute; inset: 0;
    display: flex; align-items: center; justify-content: center;
    font-size: 30px; font-weight: 700; color: var(--navy);
    letter-spacing: 1px; text-align: center;
  }
</style>
</head>
<body>
  <section class="card card--front" aria-label="Business card front">
    <div class="card__pattern" role="img" aria-label="Geometric blush pink, rose gold glitter and marble triangle pattern"></div>
    <div class="card__frame"></div>
    <div class="card__panel">
      <p class="brand-mark">Danica Pruett Interiors</p>
      <div class="person">
        <p class="person__name">Elliot Marsh</p>
        <p class="person__role">Manager</p>
      </div>
      <div class="divider"></div>
      <ul class="contacts">
        <li><svg viewBox="0 0 12 12"><path d="M2.5 1l2 2.2-1 1.3c.8 1.6 2 2.8 3.5 3.5l1.3-1L10.5 9 9.3 11C5 10.6 1.4 7 1 2.7z"/></svg>555-014-2100</li>
        <li><svg viewBox="0 0 12 12"><path d="M1 2.5h10v7H1zm1 1v.3l4 2.6 4-2.6v-.3zm0 1.5v3.5h8V5L6 7.6z"/></svg>hello@danicapruett.com</li>
        <li><svg viewBox="0 0 12 12"><circle cx="6" cy="6" r="5"/></svg>www.danicapruett.com</li>
      </ul>
      <p class="address-line">Your address, city, state, ZIP 0000</p>
    </div>
  </section>

  <section class="card card--back" aria-label="Business card back">
    <div class="card__pattern" role="img" aria-label="Geometric blush pink, rose gold glitter and marble triangle pattern"></div>
    <div class="card__frame"></div>
    <div class="card__panel">
      <p class="brand-name">Danica Pruett Interiors</p>
    </div>
  </section>
</body>
</html>
```